Create Flyer for RGB wall washers

We are launching a product that is run by an app and allows you to customize your exterior lighting at the touch of a button. We want to create the image of being technologically advanced company who is easy to work with. Looking for streamlined design which will reflect how we operate as a company. We will be printing at printmarrow.example so please have the correct format. I am looking for this to be single sided thank you for your time and submission

Target Market(s)

Residential and commercial

Industry/Entity Type

Product

Requirements
Must have
• clean layout
• easy to read
• Common fonts
• Color scheme must work with logo (we can provide a black background to logo in needed)
Nice to have
• Nicely displayed images to help sell the idea
Should not have
• Too busy background

```html
<!DOCTYPE html>
<html lang="en">
<head>
<meta charset="utf-8">
<title>Lumenway Lighting – RGB Wall Washer Flyer</title>
<link rel="stylesheet" href="https://fonts.googleapis.com/css2?family=Anton&family=Open+Sans:wght@400;600&display=swap">
<style>
  :root {
    --stage: #2b2a28;
    --flyer: #0b0c0d;
    --ink-white: #f4f6f8;
    --ink-silver: #d3dce6;
    --ink-sky: #a9d3f2;
    --ink-lime: #c8df63;
    --ink-red: #e1202b;
    --ink-logo: #9cc6ec;
    --glow-teal: #1f4f58;
    --line: #cfcfcf;
  }
  * { box-sizing: border-box; margin: 0; padding: 0; }
  html, body { width: 1200px; height: 1017px; overflow: hidden; background: var(--stage); }
  .flyer {
    position: absolute; left: 260px; top: 28px; width: 680px; height: 961px;
    background: var(--flyer); overflow: hidden; font-family: "Open Sans", sans-serif;
    box-shadow: 0 10px 40px rgba(0,0,0,.5);
  }
  .hero-backdrop {
    position: absolute; left: 0; top: 0; width: 100%; height: 430px;
    background: linear-gradient(180deg, #2a2d31 0%, #1a1c1f 55%, var(--flyer) 100%);
  }
  .brand {
    position: absolute; top: 30px; width: 100%; display: flex; justify-content: center; align-items: center; gap: 8px;
    color: var(--ink-logo); font-family: "Open Sans", sans-serif; font-weight: 600; font-size: 15px; letter-spacing: 2px; text-transform: uppercase;
  }
  .brand-mark { width: 16px; height: 16px; background: var(--ink-logo); }
  .headline {
    position: absolute; top: 62px; width: 100%; text-align: center;
    font-family: "Anton", sans-serif; font-size: 54px; line-height: 1.08; text-shadow: 0 3px 6px rgba(0,0,0,.6);
  }
  .headline .l1 { color: var(--ink-white); display: block; }
  .headline .l2 { color: var(--ink-silver); display: block; }
  .headline .l3 { color: var(--ink-sky); display: block; }
  .intro {
    position: absolute; top: 250px; left: 60px; right: 60px; text-align: center;
    font-family: "Anton", sans-serif; font-size: 18px; line-height: 1.3; color: var(--ink-lime); letter-spacing: .3px;
  }
  .call {
    position: absolute; top: 322px; width: 100%; text-align: center;
    font-family: "Anton", sans-serif; color: var(--ink-red); font-size: 62px; line-height: 1; letter-spacing: 1px;
  }
  .phone-number {
    position: absolute; top: 392px; width: 100%; text-align: center;
    font-family: "Anton", sans-serif; color: var(--ink-white); font-size: 46px; line-height: 1; letter-spacing: 2px;
  }
  .app-showcase {
    position: absolute; top: 455px; left: 150px; width: 500px; height: 240px;
    background: radial-gradient(ellipse at center, #e9ecef 0%, #9aa3aa 35%, var(--glow-teal) 65%, var(--flyer) 100%);
    border-radius: 12px;
  }
  .price-badge {
    position: absolute; top: 450px; left: 30px; width: 170px; height: 170px; border-radius: 50%;
    background: #fff; border: 6px solid #f1d2d2; box-shadow: 0 0 0 3px var(--ink-red) inset, 0 4px 12px rgba(0,0,0,.6);
    display: flex; flex-direction: column; align-items: center; justify-content: center;
    font-family: "Anton", sans-serif; color: var(--ink-red); text-align: center; line-height: 1.05;
  }
  .price-badge .from { font-size: 20px; }
  .price-badge .amount { font-size: 40px; }
  .price-badge .note { font-size: 15px; }
  .uses {
    position: absolute; top: 712px; left: 20px; right: 20px; display: flex; justify-content: space-between;
  }
  .use { width: 200px; display: flex; flex-direction: column; align-items: center; }
  .use-photo {
    width: 140px; height: 140px; border-radius: 50%; border: 3px solid #e8e8e8;
  }
  .use-photo.everyday { background: radial-gradient(circle at 50% 40%, #b8a6c9 0%, #5b4a6a 45%, #2a2020 100%); }
  .use-photo.events { background: radial-gradient(circle at 50% 40%, #d24fb0 0%, #5d3a9a 45%, #2b1d18 100%); }
  .use-photo.holiday { background: radial-gradient(circle at 50% 40%, #3fb07a 0%, #8a3a3a 50%, #2b2016 100%); }
  .use-caption {
    margin-top: 12px; width: 190px; min-height: 52px; border: 1px solid var(--line);
    display: flex; align-items: center; justify-content: center; text-align: center;
    color: var(--ink-white); font-size: 12px; font-weight: 600; line-height: 1.25; text-transform: uppercase; padding: 6px;
  }
  .use-caption.mixed { text-transform: none; font-size: 13px; }
  .website {
    position: absolute; bottom: 26px; width: 100%; text-align: center;
    color: var(--ink-white); font-size: 17px; letter-spacing: 9px;
  }
</style>
</head>
<body>
  <main class="flyer">
    <div class="hero-backdrop" role="img" aria-label="Dim photo of a house exterior at night"></div>

    <div class="brand"><span class="brand-mark"></span>Lumenway Lighting</div>

    <h1 class="headline">
      <span class="l1">Control your outdoor</span>
      <span class="l2">lighting with</span>
      <span class="l3">the touch of a button</span>
    </h1>

    <p class="intro">State-of-the-Art lighting system that will wash your exterior walls with light or landscape plantings with up-lights. Its year-round lighting at a fraction of the cost</p>

    <div class="call">CALL US TODAY</div>
    <div class="phone-number">555 010 2746</div>

    <div class="app-showcase" role="img" aria-label="Four smartphones showing the lighting control app with colour wheels and palettes"></div>

    <div class="price-badge">
      <span class="from">Starting at</span>
      <span class="amount">$799</span>
      <span class="note">including<br>installation</span>
    </div>

    <section class="uses">
      <div class="use">
        <div class="use-photo everyday" role="img" aria-label="House lit with soft white wall washers at night"></div>
        <div class="use-caption">Standard lighting<br>for everyday use</div>
      </div>
      <div class="use">
        <div class="use-photo events" role="img" aria-label="House washed in pink and purple light for a special event"></div>
        <div class="use-caption">Special events – you choose the colors and effects</div>
      </div>
      <div class="use">
        <div class="use-photo holiday" role="img" aria-label="House lit in red and green holiday colours"></div>
        <div class="use-caption mixed">Holiday lighting<br>made simple</div>
      </div>
    </section>

    <div class="website">www.lumenway-lighting.example</div>
  </main>
</body>
</html>
```